Brocure for Brindle - Social Media Management

Brindle is a Dutch company in the market of Social Media growth. We need a brochure (digital/PDF) for our company. Please see attached word doc for the text and attached logo. The initial proposal can contain just the first 4 pages text of the word doc.

We use informal language in all our communication.

Slogan: Effectieve Social Media Marketing voor professionals en ondernemers

Website: brindlesm-voorbeeld.nl

Industry/Entity Type

Digital Marketing

Contact Information for Business Card

Contact details:

Gerrit ter Hoeve
gerrit@brindlesm-voorbeeld.nl
06-19573826

```html
<!DOCTYPE html>
<html lang="nl">
<head>
<meta charset="utf-8">
<title>Brindle – Brochure Effectieve Social Media</title>
<link rel="stylesheet" href="https://fonts.googleapis.com/css2?family=Montserrat:wght@500;600;700;800&family=Open+Sans:wght@400;600;700&display=swap">
<style>
  :root{
    --orange:#f26b1d;
    --navy:#1f2b45;
    --ink:#3a3f4a;
    --page:#f3f3f3;
    --band:#e4e4e5;
    --stage:#dcdcdf;
    --line:#2b3a5c;
  }
  *{margin:0;padding:0;box-sizing:border-box}
  html,body{width:1200px;height:2271px;overflow:hidden}
  body{background:var(--stage);font-family:"Open Sans",sans-serif;color:var(--ink);position:relative}
  .spread{position:absolute;left:105px;width:990px;height:700px;display:flex;box-shadow:0 6px 24px rgba(0,0,0,.12)}
  .spread--covers{top:28px}
  .spread--inside-a{top:785px}
  .spread--inside-b{top:1542px}
  .page{position:relative;width:495px;height:700px;background:var(--page);overflow:hidden}
  .page + .page{border-left:1px solid #d4d4d6}

  /* brand name */
  .brand{display:flex;align-items:center;gap:8px;font-family:"Montserrat",sans-serif;font-weight:800;color:var(--orange);letter-spacing:.08em;text-transform:uppercase;white-space:nowrap}
  .brand__dot{width:22px;height:22px;border-radius:50%;background:var(--orange);flex:none}

  /* back cover */
  .back .brand{position:absolute;left:60px;top:420px;font-size:26px}
  .back .brand__dot{width:30px;height:30px}
  .contact{position:absolute;left:60px;top:480px}
  .contact__title{font-family:"Montserrat",sans-serif;font-weight:700;font-size:20px;color:var(--navy);padding-bottom:6px;border-bottom:2px solid var(--navy);display:inline-block;margin-bottom:16px}
  .contact__row{display:flex;align-items:center;gap:12px;font-family:"Montserrat",sans-serif;font-weight:600;font-size:15px;color:var(--navy);margin-bottom:12px}
  .contact__row svg{width:18px;height:18px;flex:none}

  /* front cover */
  .front .brand{position:absolute;left:0;right:0;top:70px;justify-content:center;font-size:24px}
  .cover-title{position:absolute;left:0;right:0;top:130px;text-align:center;font-family:"Montserrat",sans-serif;font-weight:800;font-size:44px;line-height:1.02;color:var(--orange);letter-spacing:.02em}
  .cover-sub{position:absolute;left:0;right:0;top:232px;text-align:center;font-family:"Montserrat",sans-serif;font-weight:500;font-size:15px;color:var(--navy);letter-spacing:.04em}
  .cover-art{position:absolute;left:92px;top:285px;width:310px;height:290px;border-radius:50%;background:radial-gradient(circle,#2c3a5a 0%,#3d4b6b 45%,#e8e9ec 72%)}
  .cover-url{position:absolute;left:0;right:0;bottom:50px;text-align:center;font-family:"Montserrat",sans-serif;font-weight:700;font-size:19px;letter-spacing:.16em;color:var(--orange);white-space:nowrap}

  /* inside pages */
  .inner{padding:34px 40px 0}
  .band{background:var(--band);margin:0 -40px;padding:14px 40px}
  .kicker{font-family:"Montserrat",sans-serif;font-weight:800;font-size:15px;line-height:1.25;color:var(--orange);text-transform:uppercase;margin-bottom:14px}
  .h{font-family:"Montserrat",sans-serif;font-weight:700;font-size:12.5px;color:var(--navy);margin:10px 0 4px}
  .p{font-size:8.6px;line-height:1.5;margin-bottom:4px}
  .p strong{color:var(--navy)}
  .lead-orange{font-family:"Montserrat",sans-serif;font-weight:600;font-size:10px;color:var(--orange);margin-bottom:10px}

  .platforms{display:grid;grid-template-columns:1.5fr 1fr;gap:8px 20px}
  .platform{display:flex;align-items:center;gap:8px;font-size:8.6px;font-weight:700;color:var(--navy);line-height:1.3}
  .platform__dot{width:17px;height:17px;border-radius:50%;background:var(--navy);flex:none}

  .footer{position:absolute;left:30px;right:0;bottom:26px;height:40px}
  .footer .brand{position:absolute;left:0;bottom:10px;font-size:12px}
  .footer .brand__dot{width:14px;height:14px}
  .footer__rule{position:absolute;left:110px;right:30px;bottom:26px;height:1px;background:var(--line)}
  .footer__pill{position:absolute;right:0;bottom:0;height:24px;width:262px;background:var(--navy);border-radius:12px 0 0 12px;color:#fff;font-family:"Montserrat",sans-serif;font-weight:500;font-size:10px;letter-spacing:.08em;white-space:nowrap;display:flex;align-items:center;padding-left:18px;padding-right:50px}
  .footer__num{position:absolute;right:12px;bottom:-2px;width:28px;height:28px;border-radius:50%;background:var(--orange);color:var(--navy);font-family:"Montserrat",sans-serif;font-weight:800;font-size:11px;display:flex;align-items:center;justify-content:center}

  .ribbon{position:relative;margin:8px -40px 6px 120px;background:var(--orange);color:#fff;font-family:"Montserrat",sans-serif;font-weight:700;font-size:15px;padding:7px 0 7px 30px}
  .photo{margin-top:16px;height:300px;background:linear-gradient(135deg,#1b4f9c 0%,#2f76c9 50%,#173a72 100%)}
</style>
</head>
<body>

<section class="spread spread--covers">
  <div class="page back">
    <div class="brand"><span class="brand__dot"></span>Brindle</div>
    <div class="contact">
      <div class="contact__title">Contact us</div>
      <div class="contact__row">
        <svg viewBox="0 0 24 24"><path fill="#f26b1d" d="M6.6 10.8a15 15 0 0 0 6.6 6.6l2.2-2.2a1 1 0 0 1 1-.25 11.4 11.4 0 0 0 3.6.57 1 1 0 0 1 1 1V20a1 1 0 0 1-1 1A17 17 0 0 1 3 4a1 1 0 0 1 1-1h3.5a1 1 0 0 1 1 1c0 1.25.2 2.450.57 3.57a1 1 0 0 1-.25 1z"/></svg>
        06-19573826
      </div>
      <div class="contact__row">
        <svg viewBox="0 0 24 24"><rect x="2" y="5" width="20" height="14" fill="#f26b1d"/><path d="M2 5l10 8 10-8" fill="none" stroke="#fff" stroke-width="1.6"/></svg>
        gerrit@brindlesm-voorbeeld.nl
      </div>
      <div class="contact__row">
        <svg viewBox="0 0 24 24"><circle cx="12" cy="12" r="10" fill="#f26b1d"/><path d="M2 12h20M12 2c3 3 3 17 0 20M12 2c-3 3-3 17 0 20" fill="none" stroke="#fff" stroke-width="1.2"/></svg>
        www.brindlesm-voorbeeld.nl
      </div>
    </div>
  </div>
  <div class="page front">
    <div class="brand"><span class="brand__dot"></span>Brindle</div>
    <h1 class="cover-title">EFFECTIEVE<br>SOCIAL MEDIA</h1>
    <p class="cover-sub">Marketing voor professionals en ondernemers</p>
    <div class="cover-art" role="img" aria-label="Illustratie: netwerk van social media iconen rond een laptop"></div>
    <p class="cover-url">www.brindlesm-voorbeeld.nl</p>
  </div>
</section>

<section class="spread spread--inside-a">
  <div class="page">
    <div class="inner">
      <h2 class="kicker">Social media marketing voor zakelijke<br>professionals en ondernemers</h2>
      <h3 class="h">Groei, interactie en content</h3>
      <p class="p">Je bereik vergroten, meer zichtbaarheid en daarmee meer omzet behalen. Dat is wat wij beloven. Onze aanpak combineert slimme content met actieve interactie, zodat jouw netwerk groeit.</p>
      <p class="p"><strong>(actieve interactie + relevante content) &gt; actieve volgers &gt; traffic + omzet</strong></p>
      <h3 class="h">Wie zijn wij?</h3>
      <p class="p">Wij zijn Brindle. Een team van social media experts dat je sociale netwerk activeert en het bereik vergroot. We zorgen voor echte interactie met volgers, klanten en relaties.</p>
      <p class="p"><strong>Het doel? Meer omzet. Simpel en heel meetbaar.</strong></p>
      <h3 class="h">Voor wie?</h3>
      <p class="p">Onze dienstverlening kan ingezet worden op zowel persoonlijke zakelijke profielen als op bedrijfspagina's op diverse sociale mediakanalen.</p>
      <div class="band">
        <h3 class="h">Wat doen we?</h3>
        <p class="p">Samen met jou bepalen we je doelen in de sociale netwerken. Zowel strategisch als tactisch en operationeel. Wij richten ons op het vergroten van je netwerk met de juiste volgers. Daarnaast zorgen we voor interactie die echt iets oplevert.</p>
        <p class="p">Voor zakelijke professionals verzorgen we persoonlijke branding, zodat je zichtbaar bent als autoriteit in je vakgebied. Onze diensten voor bedrijven bestaan uit de inzet van content en interactie.</p>
      </div>
    </div>
    <div class="footer">
      <div class="brand"><span class="brand__dot"></span>Brindle</div>
      <div class="footer__rule"></div>
      <div class="footer__pill">www.brindlesm-voorbeeld.nl</div>
      <div class="footer__num">01</div>
    </div>
  </div>
  <div class="page">
    <div class="inner">
      <div class="band">
        <h3 class="h">Welke platformen?</h3>
        <p class="lead-orange">We bieden onze diensten aan op alle belangrijke platformen:</p>
        <div class="platforms">
          <div class="platform"><span class="platform__dot"></span>Vakkring (bedrijfspagina's en persoonlijke profielen)</div>
          <div class="platform"><span class="platform__dot"></span>Kwetter</div>
          <div class="platform"><span class="platform__dot"></span>Buurtboek (bedrijfspagina's en groepen)</div>
          <div class="platform"><span class="platform__dot"></span>Kijkbuis</div>
          <div class="platform"><span class="platform__dot"></span>Fotomoment (bedrijfspagina's en persoonlijke profielen)</div>
          <div class="platform"><span class="platform__dot"></span>Zoekgids Bedrijf</div>
          <div class="platform"><span class="platform__dot"></span>Optioneel: Klipklap, Prikbord, Draadje en Tuimel</div>
        </div>
      </div>
      <h3 class="h">Waarom kies je voor ons?</h3>
      <p class="p">Jij hebt jouw vak, wij het onze. Als iedereen doet waar hij goed in is, worden daar allemaal beter van. Wij zijn goed in het activeren en vergroten van je sociale netwerk. Daarvoor gebruiken we een slimme mix van kennis en tools.</p>
      <p class="p">Een strategie die ervoor zorgt dat jij je kunt focussen op je corebusiness. Met als resultaat: meer traffic, meer leads, meer omzet.</p>
      <h3 class="h">Hoe lang gaan we met elkaar in zee?</h3>
      <p class="p">Een groeistrategie werkt op de lange termijn het beste als die groei organisch is. Dat vraagt dus ook een strategie voor de lange termijn. Reken op een samenwerking van minimaal een jaar om de groei echt te laten werken. Daarom vragen we ook regelmatig jouw energie en input.</p>
      <h3 class="h">Groeien op sociale media</h3>
      <p class="p">Het staat als een paal boven water: sociale media zijn een krachtig marketinginstrument. Een kans die je niet voorbij kunt laten gaan. Het geeft je de kans om je merk op te bouwen en je zicht- en vindbaarheid te verbeteren.</p>
      <p class="p">Het beheren van je sociale platforms is een tijdrovende klus. Om de online herkenbaarheid van je bedrijf te vergroten, zijn je uitingen ook nog eens slim doen.</p>
    </div>
    <div class="footer">
      <div class="brand"><span class="brand__dot"></span>Brindle</div>
      <div class="footer__rule"></div>
      <div class="footer__pill">www.brindlesm-voorbeeld.nl</div>
      <div class="footer__num">02</div>
    </div>
  </div>
</section>

<section class="spread spread--inside-b">
  <div class="page">
    <div class="inner">
      <h3 class="h">Volledig social management</h3>
      <p class="p">We bieden een compleet beheerpakket voor sociale media waarmee je betrokkenheid van volgers realiseert en tijdig alles proactief schakelen naar de volgende stap. Zo zijn we volledig betrokken.</p>
      <p class="p">We plannen, posten en reageren. Alle kanalen, specifieke inhoud en combineren online aanwezigheid om meer en meer bereik te genereren.</p>
      <h3 class="h">Volledig social management</h3>
      <p class="p">Je bent al een poos bezig met het beheren van je sociale media, maar ziet geen resultaat. Wij kijken met een frisse blik naar je kanalen en zorgen voor een heldere aanpak met meer interactie.</p>
      <div class="band">
        <h3 class="h">Groeistrategie</h3>
        <p class="p">Je bent al een poos bezig met het beheren van je sociale media, maar ziet geen commerciële resultaten. Onze specialisten maken een strategie die past bij jouw doelen en merk, zodat je meer volgers, meer likes en meer betrokkenheid krijgt.</p>
      </div>
      <div class="ribbon">Hoe werkt het?</div>
      <h3 class="h">Quick Scan&amp; advies</h3>
      <p class="p">We starten altijd met een analyse van je website en sociale kanalen. Op basis daarvan geven we je advies over de beste strategie.</p>
      <h3 class="h">Je wilt met ons in zee</h3>
      <p class="p">Als je besluit met ons in zee te gaan, dan maken we een plan op maat. Samen bepalen we de doelen en de planning, zodat je precies weet wat je kunt verwachten.</p>
      <h3 class="h">Pakketkeuze</h3>
      <p class="p">We hebben verschillende pakketten die passen bij elke fase van je bedrijf. Geen vaste kosten, gewoon helder en eerlijk.</p>
    </div>
    <div class="footer">
      <div class="brand"><span class="brand__dot"></span>Brindle</div>
      <div class="footer__rule"></div>
      <div class="footer__pill">www.brindlesm-voorbeeld.nl</div>
      <div class="footer__num">03</div>
    </div>
  </div>
  <div class="page">
    <div class="inner">
      <h3 class="h">Implementatie</h3>
      <p class="p">Natuurlijk wil je zo snel mogelijk resultaat zien. Dat willen wij ook. We werken de strategie uit in een plan en gaan voor jou aan het werk. Met de prioriteit op de gebieden die zo snel mogelijk resultaten opleveren. Omdat we graag snel zien dat onze inspanningen verschil maken.</p>
      <p class="p">We richten daarvoor de benodigde systemen in. In het begin hebben we regelmatig overleg om elkaar goed te leren kennen en de vinger aan de pols te houden.</p>
      <h3 class="h">Terugkoppeling en verbetering</h3>
      <p class="p">Iedere ondernemer is gedreven als het gaat om het behalen van resultaten. Zo ook wij. Wij doen er alles aan om onze dienstverlening zo succesvol mogelijk te laten zijn en jouw sociale doelen te behalen. We hebben regelmatig contact om de resultaten te bespreken en daar waar mogelijk te verbeteren.</p>
      <div class="photo" role="img" aria-label="Foto: kleurrijke blokjes met social media iconen op een blauwe achtergrond"></div>
    </div>
    <div class="footer">
      <div class="brand"><span class="brand__dot"></span>Brindle</div>
      <div class="footer__rule"></div>
      <div class="footer__pill">www.brindlesm-voorbeeld.nl</div>
      <div class="footer__num">04</div>
    </div>
  </div>
</section>

</body>
</html>
```